Business Card Design for Orthopaedic Surgeon

This is a double-sided glossy business card. I prefer baby blue, teal, and green as color schemes. I have my logo already (many colors that you can choose from). I have photos and examples of my old card (very bland but has the information in it). I also have one that my assistant tried to design, but the writing is too small and I don't love the formatting. But it is close!
I would like my logo to be on the business card but I'm uploading my logo in many different colors so you can choose which one looks best based on the color scheme. I also uploaded many sized headshots so you can choose the best resolution one.

Additional information:
Correct business address:
4382 NW 58th Lane, Suite 305
Tamarac, FL 33417

Everything else on both business cards are accurate.

I actually need 2 different business cards generated. One that includes my cell phone number-- Personal cell: 585-314-9062 in addition to Office phone: (954) 316-4870 and Office Fax: 954-316-4881. Again, one card would have my personal cell and one wouldn't

Overall I just think the baby blue card (uploaded) is missing something on the front--of course it is also missing my office phone/fax/personal cell. I do want my website on the front too. Email: info@wellsorthocare.example

You can use your discretion about what goes on the front vs. what goes on the back to eliminated clutter.

Oh and on the back, I would like to list "Conditions Treated" (not specialties include). The list is:
Carpal Tunnel
Trigger Finger
Ganglion Cysts
Hand Tumors
Han & Wrist Arthritis
Hand, Wrist & Elbow Tendonitis
Fractures of the Hand, Wrist, Elbow and Humerus
Nerve Injuries of the Hand, Wrist & Elbow
Microsurgery
Wrist Arthroscopy
Endoscopic Surgery

Target Market(s)

Primary care doctors, Lawyers, patients

Industry/Entity Type

Medical

Contact Information for Business Card

Please see above in project description

Colors

Designer to choose colors to be used in the design.

Requirements
Must have
• -Correct office info, Board Certified Orthopaedic Hand & Upper Extremity Surgeon
Nice to have
• Something that is classy and wow!

```html
<!DOCTYPE html>
<html lang="en">
<head>
<meta charset="utf-8">
<title>Dana Wells, MD – Business Card</title>
<link href="https://fonts.googleapis.com/css2?family=Montserrat:wght@500;600&family=Questrial&display=swap" rel="stylesheet">
<style>
  :root {
    --stage: #2a2a2c;
    --card-deep: #08262b;
    --card-mid: #0f3d42;
    --accent: #8fd3e8;
    --accent-green: #7fcfa9;
    --ink-light: #eef7f8;
    --ink-muted: #b9d9df;
    --paper: #ffffff;
    --photo-dark: #1d2a2e;
    --photo-light: #f4f6f6;
  }
  * { box-sizing: border-box; margin: 0; padding: 0; }
  html, body { width: 1200px; height: 900px; overflow: hidden; }
  body {
    background: var(--stage);
    font-family: "Questrial", sans-serif;
    position: relative;
  }
  .card {
    position: absolute;
    left: 270px;
    width: 660px;
    height: 377px;
    border-radius: 22px;
    overflow: hidden;
  }
  /* Back side */
  .card-back {
    top: 40px;
    background: linear-gradient(115deg, var(--card-deep) 0%, var(--card-mid) 55%, var(--card-deep) 100%);
  }
  .brand {
    position: absolute;
    top: 48px;
    left: 0;
    right: 0;
    display: flex;
    justify-content: center;
    align-items: center;
    gap: 16px;
  }
  .brand-ring {
    width: 54px; height: 54px;
    border: 3px solid var(--accent);
    border-radius: 50%;
  }
  .brand-name {
    font-family: "Montserrat", sans-serif;
    font-weight: 600;
    font-size: 34px;
    letter-spacing: 4px;
    color: var(--accent);
  }
  .conditions-heading {
    position: absolute;
    top: 140px;
    left: 0; right: 0;
    text-align: center;
    font-family: "Montserrat", sans-serif;
    font-weight: 600;
    font-size: 15px;
    letter-spacing: 3px;
    color: var(--accent-green);
    text-transform: uppercase;
  }
  .conditions {
    position: absolute;
    top: 178px;
    left: 0; right: 0;
    text-align: center;
    list-style: none;
    color: var(--ink-light);
    font-size: 13.5px;
    letter-spacing: 0.6px;
    line-height: 27px;
    text-transform: uppercase;
  }
  .tick { display: inline-block; width: 12px; height: 12px; vertical-align: -1px; margin: 0 6px; }

  /* Front side */
  .card-front {
    top: 460px;
    background: var(--paper);
  }
  .headshot {
    position: absolute;
    left: 0; top: 0;
    width: 320px; height: 377px;
    background: linear-gradient(180deg, var(--photo-light) 0%, #d9cfc8 30%, #6b5a52 62%, var(--photo-dark) 100%);
  }
  .info-panel {
    position: absolute;
    left: 262px;
    top: -162px;
    width: 760px;
    height: 700px;
    border-radius: 50%;
    background: linear-gradient(110deg, var(--card-deep) 0%, var(--card-mid) 60%, var(--card-deep) 100%);
  }
  .details {
    position: absolute;
    left: 330px;
    top: 34px;
    color: var(--ink-light);
  }
  .name {
    font-family: "Montserrat", sans-serif;
    font-weight: 600;
    font-size: 30px;
    letter-spacing: 1.5px;
    color: var(--accent);
    text-transform: uppercase;
    white-space: nowrap;
  }
  .title {
    margin-top: 4px;
    font-size: 15px;
    line-height: 19px;
    color: var(--ink-muted);
  }
  .contact {
    list-style: none;
    margin-top: 14px;
    font-size: 16px;
    line-height: 21px;
  }
  .contact li { display: flex; align-items: flex-start; gap: 12px; margin-bottom: 4px; white-space: nowrap; }
  .contact svg { width: 14px; height: 14px; margin-top: 3px; flex: none; fill: var(--accent-green); }
  .label { color: var(--ink-muted); }
</style>
</head>
<body>
  <svg width="0" height="0" style="position:absolute">
    <defs>
      <symbol id="icon-tick" viewBox="0 0 12 12">
        <circle cx="6" cy="6" r="6" fill="#7fcfa9"/>
        <path d="M3.2 6.2 L5.2 8 L8.8 4.2" stroke="#08262b" stroke-width="1.6" fill="none"/>
      </symbol>
    </defs>
  </svg>

  <section class="card card-back" aria-label="Card back">
    <div class="brand">
      <span class="brand-ring"></span>
      <span class="brand-name">WELLS HAND</span>
    </div>
    <h2 class="conditions-heading">Conditions Treated</h2>
    <ul class="conditions">
      <li>Carpal Tunnel<svg class="tick"><use href="#icon-tick"/></svg>Trigger Finger<svg class="tick"><use href="#icon-tick"/></svg>Ganglion Cysts</li>
      <li>Han &amp; Wrist Arthritis<svg class="tick"><use href="#icon-tick"/></svg>Hand, Wrist &amp; Elbow Tendonitis</li>
      <li>Fractures of the Hand, Wrist, Elbow &amp; Humerus<svg class="tick"><use href="#icon-tick"/></svg>Hand Tumors</li>
      <li>Nerve Injuries of the Hand, Wrist &amp; Elbow<svg class="tick"><use href="#icon-tick"/></svg>Microsurgery</li>
      <li>Wrist Arthroscopy<svg class="tick"><use href="#icon-tick"/></svg>Endoscopic Surgery</li>
    </ul>
  </section>

  <section class="card card-front" aria-label="Card front">
    <div class="headshot" role="img" aria-label="Portrait photo of the surgeon in a dark blazer on a white background"></div>
    <div class="info-panel"></div>
    <div class="details">
      <h1 class="name">Dana Wells, MD</h1>
      <p class="title">Board Certified Orthopaedic<br>Hand &amp; Upper Extremity Surgeon</p>
      <ul class="contact">
        <li><svg viewBox="0 0 14 14"><path d="M7 0a5 5 0 0 0-5 5c0 3.6 5 9 5 9s5-5.4 5-9a5 5 0 0 0-5-5zm0 7a2 2 0 1 1 0-4 2 2 0 0 1 0 4z"/></svg><span>4382 NW 58th Lane<br>Suite 305<br>Tamarac, FL 33417</span></li>
        <li><svg viewBox="0 0 14 14"><path d="M3 .5l2.2 2.7-1.3 1.9c.9 2 2.9 4 4.9 4.9l1.9-1.3 2.7 2.2-1.2 2.4C6.5 13 1 7.5.6 1.7z"/></svg><span><span class="label">Office</span> (954) 316-4870</span></li>
        <li><svg viewBox="0 0 14 14"><path d="M4 0h6a1.5 1.5 0 0 1 1.5 1.5v11A1.5 1.5 0 0 1 10 14H4a1.5 1.5 0 0 1-1.5-1.5v-11A1.5 1.5 0 0 1 4 0zm0 2v9h6V2zm3 9.6a.8.8 0 1 0 0 1.6.8.8 0 0 0 0-1.6z"/></svg><span><span class="label">Cell</span> 585-314-9062</span></li>
        <li><svg viewBox="0 0 14 14"><path d="M3 0h8v4H3zM1 5h12a1 1 0 0 1 1 1v5h-3v3H3v-3H0V6a1 1 0 0 1 1-1zm3 5v3h6v-3z"/></svg><span><span class="label">Fax</span> 954-316-4881</span></li>
        <li><svg viewBox="0 0 14 14"><path d="M0 2h14v10H0zm1.2 1.2v.3L7 7.6l5.8-4.1v-.3zM1.2 5v5.8h11.6V5L7 9.1z"/></svg><span>info@wellsorthocare.example</span></li>
        <li><svg viewBox="0 0 14 14"><path d="M7 0a7 7 0 1 0 0 14A7 7 0 0 0 7 0zm4.9 6.3H9.6a11 11 0 0 0-.9-4.5 5.6 5.6 0 0 1 3.2 4.5zM7 1.4c.6.8 1.2 2.5 1.3 4.9H5.7C5.8 3.9 6.4 2.2 7 1.4zM5.3 1.8a11 11 0 0 0-.9 4.5H2.1a5.6 5.6 0 0 1 3.2-4.5zM2.1 7.7h2.3c.1 1.8.4 3.3.9 4.5a5.6 5.6 0 0 1-3.2-4.5zM7 12.6c-.6-.8-1.2-2.5-1.3-4.9h2.6c-.1 2.4-.7 4.1-1.3 4.9zm1.7-.4c.5-1.2.8-2.7.9-4.5h2.3a5.6 5.6 0 0 1-3.2 4.5z"/></svg><span>wellsorthocare.example</span></li>
      </ul>
    </div>
  </section>
</body>
</html>
```